Healthcare technology firm needs business card layout. Logo provided.

We need a business card design for a new healthcare technology company called Mirvela.com. The logo is already done so that will be used in the design. We assist patients and their families manage their personal health finances. Our initial product is our web site membership that includes educational content on your health benefits, tools, and downloadable forms.

We would like to see designs that use our existing logo or extend the logo in a creative way. Should be very consumer friendly.

```html
<!DOCTYPE html>
<html lang="en">
<head>
<meta charset="utf-8">
<title>Mirvela Business Card</title>
<link rel="stylesheet" href="https://fonts.googleapis.com/css2?family=Open+Sans:wght@400;600;700&display=swap">
<style>
  :root {
    --backdrop: #e9e6e1;
    --brand-navy: #0a4a91;
    --brand-sky: #1f8fd6;
    --brand-green: #3cb54a;
    --paper: #ffffff;
    --ink: #111111;
    --light-text: #ffffff;
  }
  * { margin: 0; padding: 0; box-sizing: border-box; }
  html, body {
    width: 1200px; height: 1000px; overflow: hidden;
    background: var(--backdrop);
    font-family: "Open Sans", Arial, sans-serif;
  }
  .canvas { position: relative; width: 1200px; height: 1000px; }

  .card {
    position: absolute;
    width: 749px; height: 443px;
    border-radius: 13px;
    overflow: hidden;
  }

  /* Front face */
  .card-front { left: 80px; top: 44px; background: var(--brand-navy); }
  .wordmark {
    display: flex; align-items: center; gap: 14px;
    font-weight: 600; letter-spacing: 1px; line-height: 1;
    color: var(--brand-sky);
  }
  .wordmark-dot {
    border-radius: 50%;
    background: var(--brand-green);
    flex: none;
  }
  .card-front .wordmark {
    position: absolute; left: 0; right: 0; top: 128px;
    justify-content: center; font-size: 88px;
  }
  .card-front .wordmark-dot { width: 22px; height: 22px; }
  .front-tagline {
    position: absolute; left: 0; right: 0; top: 350px;
    text-align: center; color: var(--light-text);
    font-size: 26px; font-weight: 700;
  }
  .front-url {
    position: absolute; left: 0; right: 0; top: 390px;
    text-align: center; color: var(--brand-sky);
    font-size: 19px;
  }

  /* Back face */
  .card-back { left: 419px; top: 520px; background: var(--paper); }
  .back-panel { position: absolute; left: 0; top: 0; }
  .back-details {
    position: absolute; left: 41px; top: 120px;
    color: var(--light-text);
  }
  .city-list { list-style: none; font-size: 16px; line-height: 23px; }
  .contact-line {
    display: flex; align-items: center; gap: 8px;
    font-size: 16px; height: 26px;
  }
  .contact-line svg { width: 17px; height: 17px; flex: none; }
  .phones { margin-top: 24px; }
  .back-tagline {
    margin-top: 22px; margin-bottom: 4px;
    font-size: 17px; font-weight: 700;
  }
  .card-back .wordmark {
    position: absolute; left: 408px; top: 50px;
    font-size: 64px;
  }
  .card-back .wordmark-dot { width: 16px; height: 16px; }
  .holder {
    position: absolute; right: 48px; top: 280px; text-align: right;
  }
  .holder-name { color: var(--brand-sky); font-size: 35px; font-weight: 700; line-height: 1.2; }
  .holder-role { color: var(--ink); font-size: 26px; font-weight: 700; line-height: 1.1; }
</style>
</head>
<body>
<main class="canvas">

  <section class="card card-front" aria-label="Card front">
    <div class="wordmark"><span>Mirvela</span><span class="wordmark-dot"></span></div>
    <p class="front-tagline">Personal Health Finances, Health Educational</p>
    <p class="front-url">www.mirvela.com</p>
  </section>

  <section class="card card-back" aria-label="Card back">
    <svg class="back-panel" width="749" height="443" viewBox="0 0 749 443">
      <polygon points="0,0 352,0 384,216 352,443 0,443" fill="var(--brand-navy)"/>
    </svg>

    <div class="back-details">
      <ul class="city-list">
        <li>Port Elwin</li>
        <li>Maple Harbor</li>
        <li>Westvale</li>
        <li>Lake Orin</li>
      </ul>

      <div class="phones">
        <p class="contact-line">
          <svg viewBox="0 0 24 24" aria-hidden="true"><path fill="#fff" d="M6.6 10.8c1.4 2.8 3.8 5.1 6.6 6.6l2.2-2.2c.3-.3.7-.4 1-.2 1.1.4 2.3.6 3.6.6.6 0 1 .4 1 1V20c0 .6-.4 1-1 1C10.6 21 3 13.4 3 4c0-.6.4-1 1-1h3.5c.6 0 1 .4 1 1 0 1.3.2 2.5.6 3.6.1.3 0 .7-.2 1z"/></svg>
          <span>123 604 518</span>
        </p>
        <p class="contact-line">
          <svg viewBox="0 0 24 24" aria-hidden="true"><rect x="6" y="2" width="12" height="20" rx="2" fill="none" stroke="#fff" stroke-width="2"/><rect x="9" y="5" width="6" height="10" fill="#fff"/><circle cx="12" cy="18.5" r="1.2" fill="#fff"/></svg>
          <span>239-555-0147</span>
        </p>
      </div>

      <p class="back-tagline">Improving your health financially</p>
      <p class="contact-line">
        <svg viewBox="0 0 24 24" aria-hidden="true"><rect x="2" y="5" width="20" height="14" rx="2" fill="none" stroke="#fff" stroke-width="2"/><path d="M3 6l9 7 9-7" fill="none" stroke="#fff" stroke-width="2"/></svg>
        <span>firstname.lastname@mirvela.in</span>
      </p>
      <p class="contact-line">
        <svg viewBox="0 0 24 24" aria-hidden="true"><circle cx="12" cy="12" r="9" fill="none" stroke="#fff" stroke-width="2"/><ellipse cx="12" cy="12" rx="4" ry="9" fill="none" stroke="#fff" stroke-width="1.6"/><path d="M3 12h18M5 7h14M5 17h14" stroke="#fff" stroke-width="1.6"/></svg>
        <span>www.mirvela.com</span>
      </p>
    </div>

    <div class="wordmark"><span>Mirvela</span><span class="wordmark-dot"></span></div>

    <div class="holder">
      <p class="holder-name">Dana R. Holt</p>
      <p class="holder-role">CEO</p>
    </div>
  </section>

</main>
</body>
</html>
```